SKY Renting ( Website Graphic design ) small property management new business ( real estate )

I need a website designed for a new small Property Management ( no sales ) company I'm starting up soon. I have a design in mind that I like and would like to keep it quite similar to this if possible using my logo and colour scheme and slightly ALTER the layout. and maybe a little more interactive with some motion and images etc
Please see the link to show the simplicity I'm after. I want to be bold ad very clear and concise. I love the simplicity of this design but not necessarily the pages with just text on them. I would want them to be a bit more interesting with some pictures and photos. http://www.tilvanmorebay.com.au/

The branding on the site should be bold and very sharp.

My target market is the mid to high end of the rental market in Darwin Australia and should reflect "good quality, outstanding service and attention to detail, energetic, integrity, "

I will only require a few pages to start with, Home / Company Profile / Management Services / Owners information / Tenant information / Properties and About Darwin. I will be able to provide text for each of the pages but would be no more than 4-6 paragraphs apart from the management services page which would detail a number of the services we would offer. The properties page will just be a link to homefindr,com.au to show my listings and then a couple more links to owner and tenant portals, facebook page etc. It must also be responsive to mobile devices.

I would also like to include a facebook page design and build.

regards
Maren Pickett

Target Market(s)

property owners, investors, Darwin Australia, renters, ages 30 - 60, tenants

Industry/Entity Type

Property Management

Font styles to use
Other font styles liked:
• i like helvetica, but not essential

Requirements
Must have
• Clean and crisp pages, not busy , responsive to devices
• links to portals and facebook, any ability to add other links at a later date.
Nice to have
• music - must be upbeat but not over the top
Should not have
• be too busy on each page

```html
<!DOCTYPE html>
<html lang="en">
<head>
<meta charset="utf-8">
<title>SKY Renting</title>
<link rel="stylesheet" href="https://fonts.googleapis.com/css2?family=Open+Sans:wght@300;400;600&display=swap">
<style>
  :root {
    --bg-top: #3d4146;
    --bg-bottom: #18191b;
    --footer: #050505;
    --muted: #8a8d90;
    --tab: #76c5cb;
    --tab-text: #1f3436;
    --tile-brown: #362a2e;
    --tile-edge: #ffffff;
    --label: #1e3a3d;
    --card-1: #07848d;
    --card-2: #09919a;
    --card-3: #0a9ea6;
    --card-4: #0bacb3;
    --card-5: #1cbfc6;
    --card-6: #4ac8cd;
  }
  * { margin: 0; padding: 0; box-sizing: border-box; }
  html, body { width: 1200px; height: 1028px; overflow: hidden; background: var(--bg-bottom); }
  .site {
    position: relative;
    width: 1167px;
    height: 1000px;
    transform: scale(1.0283);
    transform-origin: 0 0;
    background: linear-gradient(180deg, var(--bg-top) 0%, #2a2d31 45%, var(--bg-bottom) 100%);
    font-family: "Open Sans", Arial, sans-serif;
    overflow: hidden;
  }
  .feedback-tab {
    position: absolute;
    left: 943px; top: 0;
    width: 100px; height: 34px;
    background: var(--tab);
    border: 1px solid #a9e0e4;
    border-top: none;
    border-radius: 0 0 4px 4px;
    color: var(--tab-text);
    font-size: 13px; font-weight: 600;
    letter-spacing: 0.3px;
    text-align: center;
    line-height: 33px;
  }
  .menu-stage { position: absolute; left: 0; top: 0; }
  .card-label {
    font-family: "Open Sans", Arial, sans-serif;
    font-size: 15px;
    fill: var(--label);
    letter-spacing: 0.2px;
  }
  .brand-name {
    font-family: "Open Sans", Arial, sans-serif;
    font-weight: 300;
    font-size: 62px;
    fill: #ffffff;
  }
  .site-footer {
    position: absolute;
    left: 0; top: 950px;
    width: 1167px; height: 50px;
    background: var(--footer);
    color: var(--muted);
    font-size: 11px;
  }
  .copyright { position: absolute; left: 124px; top: 18px; }
  .sound-toggle { position: absolute; left: 246px; top: 14px; }
  .social-links { position: absolute; left: 962px; top: 14px; display: flex; gap: 22px; }
  .social-dot { width: 22px; height: 22px; border-radius: 50%; background: #3e4043; }
</style>
</head>
<body>
<div class="site">
  <div class="feedback-tab">FEEDBACK</div>

  <svg class="menu-stage" width="1167" height="950" viewBox="0 0 1167 950">
    <defs>
      <linearGradient id="reflect-fade" x1="0" y1="0" x2="0" y2="1">
        <stop offset="0" stop-color="#fff" stop-opacity="0.35"/>
        <stop offset="0.35" stop-color="#fff" stop-opacity="0"/>
      </linearGradient>
      <mask id="reflect-mask" maskUnits="userSpaceOnUse" x="0" y="618" width="1167" height="340">
        <rect x="0" y="618" width="1167" height="340" fill="url(#reflect-fade)"/>
      </mask>
      <filter id="card-shadow" x="-20%" y="-20%" width="140%" height="140%">
        <feDropShadow dx="0" dy="2" stdDeviation="2" flood-color="#000" flood-opacity="0.35"/>
      </filter>
      <g id="menu-deck">
        <g transform="translate(764,391) rotate(57.7)" filter="url(#card-shadow)">
          <rect x="-165" y="-165" width="330" height="330" rx="5" fill="var(--card-6)"/>
          <text class="card-label" x="-150" y="-146">CONTACT US</text>
        </g>
        <g transform="translate(704,391) rotate(57.7)" filter="url(#card-shadow)">
          <rect x="-165" y="-165" width="330" height="330" rx="5" fill="var(--card-5)"/>
          <text class="card-label" x="-150" y="-146">PROPERTIES &amp; ABOUT DARWIN</text>
        </g>
        <g transform="translate(644,391) rotate(57.7)" filter="url(#card-shadow)">
          <rect x="-165" y="-165" width="330" height="330" rx="5" fill="var(--card-4)"/>
          <text class="card-label" x="-150" y="-146">TENANT INFORMATION</text>
        </g>
        <g transform="translate(584,391) rotate(57.7)" filter="url(#card-shadow)">
          <rect x="-165" y="-165" width="330" height="330" rx="5" fill="var(--card-3)"/>
          <text class="card-label" x="-150" y="-146">OWNERS INFORMATION</text>
        </g>
        <g transform="translate(524,391) rotate(57.7)" filter="url(#card-shadow)">
          <rect x="-165" y="-165" width="330" height="330" rx="5" fill="var(--card-2)"/>
          <text class="card-label" x="-150" y="-146">MANAGEMENT SERVICES</text>
        </g>
        <g transform="translate(464,391) rotate(57.7)" filter="url(#card-shadow)">
          <rect x="-165" y="-165" width="330" height="330" rx="5" fill="var(--card-1)"/>
          <text class="card-label" x="-150" y="-146">COMPANY PROFILE</text>
        </g>
        <g transform="translate(404,391) rotate(57.7)">
          <rect x="-165" y="-165" width="330" height="330" rx="3" fill="var(--tile-brown)" stroke="var(--tile-edge)" stroke-width="3.5"/>
        </g>
      </g>
    </defs>

    <g class="deck-reflection" mask="url(#reflect-mask)">
      <use href="#menu-deck" transform="translate(0,1240) scale(1,-1)"/>
    </g>

    <use href="#menu-deck"/>

    <g class="brand">
      <text class="brand-name" x="300" y="340">SKY</text>
      <text class="brand-name" x="300" y="405">Renting</text>
    </g>
  </svg>

  <footer class="site-footer">
    <span class="copyright">Copyright © 2015</span>
    <svg class="sound-toggle" width="28" height="22" viewBox="0 0 28 22" aria-label="Sound on">
      <path d="M2 7h5l6-5v18l-6-5H2z" fill="#55585b"/>
      <path d="M17 7a5 5 0 0 1 0 8M20 4a9 9 0 0 1 0 14" fill="none" stroke="#55585b" stroke-width="2" stroke-linecap="round"/>
    </svg>
    <div class="social-links">
      <span class="social-dot" role="img" aria-label="Social page link"></span>
      <span class="social-dot" role="img" aria-label="Social feed link"></span>
    </div>
  </footer>
</div>
</body>
</html>
```